Business card for denture clinic Gumlyssa

We need a new business card with our new logo. We are a denture clinic in New Zealand with our target market being 45+ years old. We would need a space on the back to write our patients next appointment on. We would space for only one appointment rather than a list. We will attach a photo showing an example of this. But of course, we would like to see your twist on this. We want it to be bold and easy to read and a good mixture of professional but modern. We have attached our logo to be used on the card.

Target Market(s)

People aged 45+ needing dentures

Industry/Entity Type

Dental

Contact Information for Business Card

We want our logo on the front and the space to write an appointment on the back. I've attached an example our our old business card showing this. We need to have the technicians details on the front.

Font styles to use
Sans Serif

Colors
0255a3
919191
fbfbfb

Requirements
Must have
• The following details:
• Ravi Pelling BDT, PGDipCDentTech Marlow
• Dental Prosthetist
• Phone numbers: 0800 47 2150
• 09 571 3294
• Email: ravi@gumlyssa.co.nz
• www.gumlyssa.co.nz
• Address: 418 Whiroa Road
• Kauriwhenua East
• Auckland 0610
Nice to have
• We would like our business cards to have more than just two colours as we want them to be more vibrant. We have uploaded an example of a business card we liked that showed this.

```html
<!DOCTYPE html>
<html lang="en">
<head>
<meta charset="utf-8">
<title>Gumlyssa – Business Card</title>
<link href="https://fonts.googleapis.com/css2?family=Arimo:wght@400;700&display=swap" rel="stylesheet">
<style>
  :root{
    --brand-blue:#0255a3;
    --mid-blue:#1a78c2;
    --soft-blue:#6fa6d2;
    --pale-blue:#d6e4f0;
    --grey:#919191;
    --ink:#2a2a2a;
    --paper:#fbfbfb;
    --stage:#2b2b2b;
  }
  *{margin:0;padding:0;box-sizing:border-box}
  html,body{width:1200px;height:997px;overflow:hidden}
  body{background:var(--stage);font-family:"Arimo",Arial,sans-serif;position:relative}

  .card{position:absolute;left:250px;width:700px;height:428px;border-radius:22px;overflow:hidden;background:var(--paper)}
  .card--back{top:48px}
  .card--front{top:516px}

  /* back */
  .back-pattern{position:absolute;inset:0;background:linear-gradient(135deg,#e4edf5,var(--pale-blue))}
  .appointment-panel{position:absolute;left:90px;top:62px;width:520px;height:304px;background:var(--mid-blue);text-align:center;color:#fff}
  .panel-mark{display:flex;align-items:center;justify-content:center;gap:12px;margin-top:46px}
  .panel-mark .mark-square{width:30px;height:30px;background:#fff}
  .wordmark{font-family:"Arimo",Arial,sans-serif;font-weight:400;text-transform:uppercase;letter-spacing:2px}
  .panel-mark .wordmark{font-size:34px;color:#fff}
  .appointment-heading{margin-top:22px;font-size:15px;font-weight:700;letter-spacing:1px;color:#10233a}
  .appointment-line{display:flex;align-items:flex-end;justify-content:center;gap:12px;margin-top:26px;font-size:14px;letter-spacing:1.5px;color:#cfe2f4}
  .appointment-line .write-space{width:250px;border-bottom:2px dotted #10233a;height:18px}

  /* front */
  .mark-decoration{position:absolute;left:340px;top:20px;width:330px;height:360px;border-radius:48% 52% 40% 60%/55% 50% 50% 45%;background:radial-gradient(circle at 50% 45%,rgba(111,166,210,.15),rgba(111,166,210,.55))}
  .front-mark{position:absolute;left:44px;top:40px}
  .front-mark .mark-square{width:52px;height:52px;background:var(--brand-blue);margin-left:118px}
  .front-mark .wordmark{display:block;margin-top:14px;font-size:40px;color:var(--brand-blue)}
  .accent-bar{position:absolute;left:0;top:200px;width:22px;height:66px;background:var(--brand-blue)}
  .technician{position:absolute;left:42px;top:184px;color:var(--ink)}
  .technician .name{font-size:22px;font-weight:700;letter-spacing:2px;color:var(--brand-blue);text-transform:uppercase}
  .technician .credentials,.technician .role{font-size:16px;line-height:20px}
  .address{position:absolute;left:42px;top:266px;font-size:17px;font-weight:700;line-height:22px;color:var(--mid-blue)}
  .contact-list{position:absolute;left:42px;top:322px;list-style:none;font-size:17px;color:var(--ink);letter-spacing:1px}
  .contact-list li{display:flex;align-items:center;gap:12px;height:30px}
  .contact-list svg{width:20px;height:20px;flex:none}
  .website{position:absolute;right:36px;top:262px;font-size:17px;font-weight:700;letter-spacing:.5px;color:#111}
</style>
</head>
<body>

<section class="card card--back" aria-label="Business card back">
  <div class="back-pattern" role="img" aria-label="Light blue checkered background pattern"></div>
  <div class="appointment-panel">
    <div class="panel-mark"><span class="mark-square"></span><span class="wordmark">Gumlyssa</span></div>
    <p class="appointment-heading">YOUR NEXT APPOINTMENT WITH US</p>
    <div class="appointment-line"><span>TIME</span><span class="write-space"></span></div>
    <div class="appointment-line"><span>DATE</span><span class="write-space"></span></div>
  </div>
</section>

<section class="card card--front" aria-label="Business card front">
  <div class="mark-decoration" role="img" aria-label="Large faint brand mark decoration"></div>
  <div class="front-mark"><div class="mark-square"></div><span class="wordmark">Gumlyssa</span></div>
  <div class="accent-bar"></div>
  <div class="technician">
    <p class="name">Ravi Pelling</p>
    <p class="credentials">PGDipCDentTech Marlow</p>
    <p class="role">Dental Prosthetist</p>
  </div>
  <p class="address">418 Whiroa Road Kauriwhenua<br>East Auckland 0610</p>
  <ul class="contact-list">
    <li><svg viewBox="0 0 20 20"><circle cx="10" cy="10" r="10" fill="#0255a3"/><path d="M6 5.5c1-.6 1.6 0 2 .9l.5 1.2c.2.5-.2 1-.6 1.3.5 1.2 1.3 2 2.4 2.5.3-.4.8-.8 1.3-.6l1.2.5c.9.4 1.5 1 .9 2-1 1.5-3.5 1-5.6-1.1S4.5 6.5 6 5.5z" fill="#fff"/></svg>0800 47 2150</li>
    <li><svg viewBox="0 0 20 20"><circle cx="10" cy="10" r="10" fill="#0255a3"/><path d="M6 5.5c1-.6 1.6 0 2 .9l.5 1.2c.2.5-.2 1-.6 1.3.5 1.2 1.3 2 2.4 2.5.3-.4.8-.8 1.3-.6l1.2.5c.9.4 1.5 1 .9 2-1 1.5-3.5 1-5.6-1.1S4.5 6.5 6 5.5z" fill="#fff"/></svg>09 571 3294</li>
    <li><svg viewBox="0 0 20 20"><circle cx="10" cy="10" r="10" fill="#0255a3"/><rect x="5" y="6.5" width="10" height="7" fill="#fff"/><path d="M5 6.5l5 4 5-4" fill="none" stroke="#0255a3" stroke-width="1.2"/></svg>ravi@gumlyssa.co.nz</li>
  </ul>
  <p class="website">www.gumlyssa.co.nz</p>
</section>

</body>
</html>
```